Licensed School Psychologist Business Card Design (may be single or double sided)

In an empathetic and nurturing environment, I conduct comprehensive psycho-educational evaluations for children and adolescents who may be experiencing academic, social/emotional challenges, and stressors in their lives. Given the collection of data and information, recommendations, supports, and strategies are created and tailored to the strengths and weaknesses of the children/adolescents as well as their families.

Industry/Entity Type

Business

Contact Information for Business Card

Bright-Path Learning Assessments
Mona Velkrist, MEd; MA
Licensed School Psychologist
482 Tarnby Crescent, Suite #3
Fernwick, VA 23990
P: 757 918-2073 F: 757 918-2150

```html
<!DOCTYPE html>
<html lang="en">
<head>
<meta charset="utf-8">
<title>Bright-Path Learning Assessments – Business Card</title>
<link href="https://fonts.googleapis.com/css2?family=Open+Sans:wght@400;600;700;800&display=swap" rel="stylesheet">
<style>
  :root {
    --stage: #a6a6a6;
    --paper: #ffffff;
    --ink: #222222;
    --brand-red: #c21f28;
    --on-dark: #ffffff;
  }
  * { box-sizing: border-box; margin: 0; padding: 0; }
  html, body { width: 1200px; height: 800px; overflow: hidden; }
  body {
    background: var(--stage);
    font-family: "Open Sans", Arial, sans-serif;
    position: relative;
  }
  .card {
    position: absolute;
    top: 246px;
    width: 540px;
    height: 309px;
    overflow: hidden;
    box-shadow: 0 6px 18px rgba(0,0,0,0.25);
  }
  .card--front { left: 40px; background: var(--paper); }
  .card--back { left: 620px; background: var(--ink); }
  .card__shapes { position: absolute; inset: 0; width: 100%; height: 100%; }

  .wordmark { position: absolute; line-height: 1; }
  .wordmark__name { font-weight: 800; letter-spacing: 0.2px; }
  .wordmark__tagline { font-weight: 400; letter-spacing: 2.6px; }

  .card--front .wordmark { left: 40px; top: 64px; }
  .card--front .wordmark__name { font-size: 31px; color: var(--ink); }
  .card--front .wordmark__tagline { font-size: 17px; color: var(--brand-red); margin-top: 2px; }

  .holder { position: absolute; right: 22px; top: 134px; text-align: right; color: var(--on-dark); }
  .holder__name { font-size: 19px; font-weight: 800; letter-spacing: 1.4px; }
  .holder__title { font-size: 9px; font-weight: 600; letter-spacing: 2px; margin-top: 1px; }

  .contact { position: absolute; left: 44px; top: 168px; color: var(--on-dark); }
  .contact__address { font-size: 13.5px; line-height: 17px; font-weight: 400; }
  .contact__lines { list-style: none; margin-top: 8px; padding-left: 14px; }
  .contact__line { display: flex; align-items: center; gap: 12px; font-size: 15px; font-weight: 700; height: 24px; }
  .contact__icon { width: 18px; height: 18px; fill: var(--brand-red); }

  .card--back .wordmark { right: 30px; top: 122px; text-align: right; color: var(--on-dark); }
  .card--back .wordmark__name { font-size: 33px; }
  .card--back .wordmark__tagline { font-size: 17px; margin-top: 3px; }
</style>
</head>
<body>

<section class="card card--front" aria-label="Business card front">
  <svg class="card__shapes" viewBox="0 0 540 309" aria-hidden="true">
    <polygon points="266,118 540,118 540,190 393,190" fill="var(--brand-red)"/>
    <polygon points="0,160 318,160 392,202 540,202 540,285 0,285" fill="var(--ink)"/>
  </svg>

  <div class="wordmark">
    <div class="wordmark__name">Bright-Path</div>
    <div class="wordmark__tagline">Learning Assessments</div>
  </div>

  <div class="holder">
    <div class="holder__name">Mona Velkrist</div>
    <div class="holder__title">MED / DOCTOR</div>
  </div>

  <div class="contact">
    <p class="contact__address">MA Licensed School<br>Psychologist 482 Tarnby Crescent,<br>Suite #3 Fernwick, VA 23990</p>
    <ul class="contact__lines">
      <li class="contact__line">
        <svg class="contact__icon" viewBox="0 0 24 24" aria-label="Phone"><path d="M2 8c0-2 4-4 10-4s10 2 10 4v2h-5V8c-1-.7-3-1-5-1s-4 .3-5 1v2H2z"/><path d="M6 11h12l3 9H3z"/><circle cx="12" cy="15.5" r="2.4" fill="var(--ink)"/></svg>
        <span>757 918-2073</span>
      </li>
      <li class="contact__line">
        <svg class="contact__icon" viewBox="0 0 24 24" aria-label="Fax"><rect x="6" y="2" width="12" height="6"/><rect x="2" y="9" width="20" height="9" rx="2"/><rect x="6" y="15" width="12" height="7" fill="var(--brand-red)" stroke="var(--ink)" stroke-width="1.5"/></svg>
        <span>757 918-2150</span>
      </li>
    </ul>
  </div>
</section>

<section class="card card--back" aria-label="Business card back">
  <svg class="card__shapes" viewBox="0 0 540 309" aria-hidden="true">
    <polygon points="165,92 540,92 540,212 290,212" fill="var(--brand-red)"/>
    <polygon points="0,110 140,110 262,232 0,232" fill="var(--brand-red)"/>
  </svg>

  <div class="wordmark">
    <div class="wordmark__name">Bright-Path</div>
    <div class="wordmark__tagline">Learning Assessments</div>
  </div>
</section>

</body>
</html>
```